Exciting Personal Development Book Cover: FIND ZEN NOW!

Design a Book Cover for my personal development book.
Title: Find Zen Now!
Author: Marcus Telly
Tagline: A real-life solution to get unstuck and break free

My picture must make up the front cover as I need to build my brand and people should recognise me on book shelves. Bold and catchy. How you do it is up to you. There must be space for a short testimonial from a famous person who is currently reading my book. I uploaded a sample of what I made in Photoshop but I don't have design skills.

I've added a PDF of my book so you can read the chapter index and introduction to get a sense of the content.

Target Market(s)

Personal Development Self-Help Market

Industry/Entity Type

Personal Development

Font styles to use
Serif
Sans Serif

Requirements
Must have
• My picture as hero image on cover.
Nice to have
• Must have Title, Tagline and my author name. If possible ZEN stands for 'Zeal, Energy & Nerve' If there is a way to fit this somewhere great. If it's too much then it can go somewhere on the back.

```html
<!DOCTYPE html>
<html lang="en">
<head>
<meta charset="utf-8">
<title>Find Zen Now! — Book Cover</title>
<link rel="stylesheet" href="https://fonts.googleapis.com/css2?family=Bebas+Neue&family=Noto+Serif:wght@700&display=swap">
<style>
  :root {
    --backdrop: #e9dccb;
    --navy: #1a2163;
    --navy-deep: #0b1150;
    --white: #ffffff;
    --slate-dark: #5c6165;
    --slate-light: #8b9196;
    --photo-light: #e8e6e3;
    --photo-skin: #b98c72;
  }
  * { margin: 0; padding: 0; box-sizing: border-box; }
  html, body { width: 1200px; height: 857px; overflow: hidden; }
  body {
    background: var(--backdrop);
    position: relative;
    font-family: "Bebas Neue", "Arial Narrow", sans-serif;
  }
  .cover {
    position: absolute;
    top: 132px;
    width: 420px;
    height: 592px;
    overflow: hidden;
    background: linear-gradient(180deg, var(--slate-dark) 0%, var(--slate-light) 40%, var(--slate-dark) 100%);
    box-shadow: 0 10px 28px rgba(0,0,0,0.25);
  }
  .cover--back { left: 160px; }
  .cover--front { left: 620px; }

  /* Back cover */
  .back-title {
    position: absolute;
    top: 22px;
    left: 34px;
    right: 34px;
    font-size: 72px;
    font-weight: 400;
    line-height: 1;
    letter-spacing: 1px;
    color: var(--white);
    white-space: nowrap;
  }
  .back-title .accent { color: var(--navy-deep); }
  .blurb {
    position: absolute;
    left: 30px;
    width: 360px;
    font-family: "Noto Serif", Georgia, serif;
    font-weight: 700;
    font-size: 11.6px;
    line-height: 1.6;
    color: var(--white);
    text-align: center;
  }
  .blurb--one { top: 120px; }
  .blurb--two { top: 226px; }
  .blurb--three { top: 332px; }
  .author-photo {
    position: absolute;
    left: 16px;
    top: 466px;
    width: 134px;
    height: 112px;
    background: var(--navy-deep);
    overflow: hidden;
  }
  .author-photo .portrait {
    position: absolute;
    left: 0; right: 0; bottom: 0; top: 6px;
    background: radial-gradient(ellipse 40% 35% at 50% 38%, var(--photo-skin) 0%, rgba(185,140,114,0) 100%),
                linear-gradient(180deg, rgba(11,17,80,0) 55%, var(--photo-light) 56%);
  }
  .author-bio {
    position: absolute;
    left: 162px;
    top: 490px;
    width: 236px;
    font-family: "Noto Serif", Georgia, serif;
    font-weight: 700;
    font-size: 7.6px;
    line-height: 1.65;
    color: var(--white);
    text-align: center;
  }
  .back-band {
    position: absolute;
    left: 0; right: 0; bottom: 0;
    height: 14px;
    background: var(--navy-deep);
  }

  /* Front cover */
  .testimonial {
    position: absolute;
    top: 22px;
    left: 22px;
    right: 16px;
    font-size: 14px;
    letter-spacing: 0.3px;
    color: var(--navy);
    white-space: nowrap;
  }
  .testimonial .source { color: var(--white); }
  .hero-photo {
    position: absolute;
    left: 214px;
    top: 78px;
    width: 206px;
    height: 462px;
    background:
      radial-gradient(ellipse 34% 18% at 48% 16%, var(--photo-skin) 0%, rgba(185,140,114,0) 100%),
      radial-gradient(ellipse 55% 45% at 60% 70%, var(--photo-light) 0%, rgba(232,230,227,0) 100%),
      linear-gradient(180deg, rgba(139,145,150,0) 0%, rgba(232,230,227,0.55) 45%, rgba(232,230,227,0.8) 100%);
  }
  .front-title {
    position: absolute;
    top: 92px;
    left: 24px;
    font-size: 124px;
    font-weight: 400;
    line-height: 0.86;
    color: var(--white);
  }
  .front-title .line { display: block; }
  .front-title .accent { color: var(--navy); }
  .author-name {
    position: absolute;
    top: 424px;
    left: 132px;
    font-size: 46px;
    line-height: 0.92;
    color: var(--white);
    letter-spacing: 0.5px;
  }
  .tagline-band {
    position: absolute;
    left: 0; right: 0; bottom: 0;
    height: 52px;
    background: var(--navy);
    display: flex;
    align-items: center;
    justify-content: center;
  }
  .tagline {
    font-size: 19px;
    letter-spacing: 0.8px;
    color: var(--white);
    white-space: nowrap;
  }
</style>
</head>
<body>

  <section class="cover cover--back" aria-label="Back cover">
    <h2 class="back-title"><span class="accent">FIND</span> ZEN NOW!</h2>
    <p class="blurb blurb--one">Lorem ipsum dolor sit amet, consectetur adipiscing elit, sed do eiusmod tempor incididunt ut labore et dolore magna aliqua. Quis ipsum suspendisse ultrices gravida. Risus commodo viverra maecenas accumsan lacus vel facilisis.</p>
    <p class="blurb blurb--two">Lorem ipsum dolor sit amet, consectetur adipiscing elit, sed do eiusmod tempor incididunt ut labore et dolore magna aliqua. Quis ipsum suspendisse ultrices gravida. Risus commodo viverra maecenas accumsan lacus vel facilisis.</p>
    <p class="blurb blurb--three">Lorem ipsum dolor sit amet, consectetur adipiscing elit, sed do eiusmod tempor incididunt ut labore et dolore magna aliqua. Quis ipsum suspendisse ultrices gravida. Risus commodo viverra maecenas accumsan lacus vel facilisis.</p>
    <div class="author-photo">
      <div class="portrait" role="img" aria-label="Portrait photo of author Marcus Telly smiling in a white shirt"></div>
    </div>
    <p class="author-bio">Lorem ipsum dolor sit amet, consectetur adipiscing elit, sed do eiusmod tempor incididunt ut labore et dolore magna aliqua. Quis ipsum suspendisse ultrices gravida. Risus commodo viverra maecenas accumsan lacus vel facilisis.</p>
    <div class="back-band"></div>
  </section>

  <section class="cover cover--front" aria-label="Front cover">
    <div class="hero-photo" role="img" aria-label="Hero photo of author Marcus Telly smiling, white shirt with rolled sleeves and tattooed forearms"></div>
    <p class="testimonial">“LOREM IPSUM DOLOR SIT AMET, CONSECTETUR ADIP” <span class="source">-PERSON READING BOOK</span></p>
    <h1 class="front-title">
      <span class="line accent">FIND</span>
      <span class="line">ZEN</span>
      <span class="line">NOW!</span>
    </h1>
    <p class="author-name">MARCUS<br>TELLY</p>
    <div class="tagline-band">
      <p class="tagline">A REAL-LIFE SOLUTION TO GET UNSTUCK AND BREAK FREE</p>
    </div>
  </section>

</body>
</html>
```